Name Card Design

Looking to create a card for my business. I am a personal stylist, my business is clothes, shoes and everything to do with looking fashion forward. I help people achieve the most polished look with cloths and grooming. I would like my card to be a reflection of my qualities which are: poise, elegance, creativity and fairness.
Things I like a simple yet expensive looking, sometimes less simple but highly creative and different catches my eye. For instance I saw a card with lace trimming at the bottom, it made me think about the business that person was in. I don't like childish designs with butterflies, trees, flowers, etc.
Here is my site www.Marta-Vosel.example for your perusal

On the card it should have the following info
Marta Vosel
personal stylist
www.Marta-Vosel.example
(+65) 482-30857
Facebook page: Ringthelook

Back of the card:
Wardrobe weeding
Personal shopping
Style consultation

Target Market(s)

mostly working women

Industry/Entity Type

Fashion

Font styles to use
Serif
Sans Serif

Requirements
Should not have
• butterflies, flowers, feathers, etc

```html
<!DOCTYPE html>
<html lang="en">
<head>
<meta charset="utf-8">
<title>Marta Vosel — Personal Stylist</title>
<link rel="stylesheet" href="https://fonts.googleapis.com/css2?family=Pinyon+Script&family=Source+Sans+3:wght@400;700&display=swap">
<style>
  :root {
    --backdrop: #e9e7e4;
    --card: #ffffff;
    --ink: #111111;
    --ink-soft: #333333;
    --band: #3b3b3b;
    --band-text: #f2f2f2;
    --rule: #bdbdbd;
    --silver-light: #f4f4f4;
    --silver-dark: #8c8c8c;
  }
  html, body {
    margin: 0;
    width: 1200px;
    height: 767px;
    overflow: hidden;
    background: var(--backdrop);
  }
  .canvas {
    position: relative;
    width: 1200px;
    height: 767px;
  }
  .card {
    position: absolute;
    left: 88px;
    top: 88px;
    width: 1027px;
    height: 590px;
    border-radius: 46px;
    background: var(--card);
    overflow: hidden;
    box-shadow: 0 2px 8px rgba(0,0,0,0.15);
  }
  .card__band {
    position: absolute;
    inset: 0;
    width: 1027px;
    height: 590px;
  }
  .brand {
    position: absolute;
    left: 0;
    right: 0;
    text-align: center;
    font-family: "Pinyon Script", cursive;
    color: var(--ink);
  }
  .brand__name {
    top: 10px;
    font-size: 118px;
    line-height: 1.2;
    letter-spacing: -1px;
    padding-left: 0;
  }
  .brand__title {
    top: 152px;
    font-size: 36px;
    line-height: 1.2;
    color: var(--ink-soft);
    padding-left: 2px;
  }
  .services {
    position: absolute;
    top: 292px;
    left: 0;
    right: 0;
    display: flex;
    justify-content: center;
    align-items: center;
    gap: 14px;
    font-family: "Source Sans 3", sans-serif;
    font-weight: 700;
    font-size: 29px;
    color: var(--ink-soft);
  }
  .services__divider {
    width: 1px;
    height: 14px;
    background: var(--rule);
  }
  .contacts {
    position: absolute;
    top: 483px;
    left: 0;
    right: 0;
    display: flex;
    justify-content: center;
    align-items: center;
    gap: 8px;
    font-family: "Source Sans 3", sans-serif;
    font-weight: 400;
    font-size: 28px;
    color: var(--band-text);
  }
  .contacts__item {
    display: flex;
    align-items: center;
    gap: 7px;
  }
  .contacts__icon {
    width: 20px;
    height: 20px;
    flex: none;
  }
  .contacts__dot {
    width: 18px;
    height: 18px;
    border-radius: 50%;
    background: var(--band-text);
    flex: none;
  }
</style>
</head>
<body>
<main class="canvas">
  <section class="card">
    <svg class="card__band" viewBox="0 0 1027 590" aria-hidden="true">
      <defs>
        <linearGradient id="silverSweep" x1="0" y1="0" x2="1" y2="0">
          <stop offset="0" stop-color="var(--silver-dark)"/>
          <stop offset="0.5" stop-color="var(--silver-light)"/>
          <stop offset="1" stop-color="var(--silver-dark)"/>
        </linearGradient>
      </defs>
      <path d="M0,474 Q520,278 1027,460 Q520,300 0,474 Z" fill="url(#silverSweep)"/>
      <path d="M0,480 Q520,308 1027,465 L1027,590 L0,590 Z" fill="var(--band)"/>
    </svg>

    <h1 class="brand brand__name" style="margin:0;font-weight:400;">Marta Vosel</h1>
    <p class="brand brand__title" style="margin:0;">Personal Stylist</p>

    <ul class="services" style="margin:0;padding:0;list-style:none;">
      <li>Wardrobe Weeding</li>
      <li class="services__divider" aria-hidden="true"></li>
      <li>Personal Shopping</li>
      <li class="services__divider" aria-hidden="true"></li>
      <li>Style consultation</li>
    </ul>

    <div class="contacts">
      <span class="contacts__item">
        <svg class="contacts__icon" viewBox="0 0 20 20" aria-hidden="true">
          <circle cx="10" cy="10" r="8.5" fill="none" stroke="var(--band-text)" stroke-width="1.4"/>
          <path d="M7 5.5 Q5 8 7.5 12 Q10 15.5 13 14.5 L12 12.5 L10.6 13 Q8.5 11 8.2 8.2 L9.5 7.5 Z" fill="var(--band-text)"/>
        </svg>
        (+65) 482-30857
      </span>
      <span class="contacts__item">
        <svg class="contacts__icon" viewBox="0 0 20 20" aria-hidden="true">
          <g fill="none" stroke="var(--band-text)" stroke-width="1.3">
            <circle cx="10" cy="10" r="8.5"/>
            <ellipse cx="10" cy="10" rx="3.8" ry="8.5"/>
            <line x1="1.5" y1="10" x2="18.5" y2="10"/>
            <line x1="3" y1="5.5" x2="17" y2="5.5"/>
            <line x1="3" y1="14.5" x2="17" y2="14.5"/>
          </g>
        </svg>
        www.Marta-Vosel.example
      </span>
      <span class="contacts__item">
        <span class="contacts__dot" aria-hidden="true"></span>
        Ringthelook
      </span>
    </div>
  </section>
</main>
</body>
</html>
```